Need a design package for hair towels wrap

We need package design for hair towel wrap ( 3 pack) brand name is The Vostra. We are looking for simple, contemporary and unique design, color palette 2-3 colors. Paper Box size is 9*8*3 inches with PVC window.Actual picture of the product won't be on the package.Attached Brand Logo and description for the package. Barcode needed to be included on the design package.It will be provided later. Attached sample of the box from manufacturer, and instruction for towel wrap which idea I like, if you could make something similar to it, would be great.

Target Market(s)

Kestrel

Industry/Entity Type

Hair

Colors
848484
f5f5f5
faa54b
333333

Requirements
Must have
• Clean, contemporary design.

```html
<!DOCTYPE html>
<html lang="en">
<head>
<meta charset="utf-8">
<title>The Vostra — Hair Towel Wrap Box Dieline</title>
<link rel="stylesheet" href="https://fonts.googleapis.com/css2?family=Montserrat:wght@400;600&family=Playfair+Display:wght@700&display=swap">
<style>
  :root {
    --orange: #faa54b;
    --charcoal: #333333;
    --grey: #848484;
    --paper: #f5f5f5;
    --backdrop: #cdd6d2;
  }
  html, body {
    margin: 0;
    padding: 0;
    width: 1200px;
    height: 841px;
    overflow: hidden;
    background: var(--backdrop);
  }
  .artboard { display: block; width: 1200px; height: 841px; }
  .panel { fill: var(--paper); }
  .band { fill: var(--orange); }
  .spine { fill: var(--charcoal); }
  .window { stroke: none; }
  .tagline {
    font-family: "Playfair Display", Georgia, serif;
    font-weight: 700;
    font-size: 12.5px;
    fill: var(--paper);
    text-anchor: middle;
  }
  .brand-name {
    font-family: "Montserrat", Arial, sans-serif;
    font-weight: 600;
    font-size: 22px;
    fill: var(--grey);
    letter-spacing: 0.5px;
  }
  .product-line {
    font-family: "Montserrat", Arial, sans-serif;
    font-size: 7px;
    fill: var(--paper);
    text-anchor: end;
  }
  .feature-list {
    font-family: "Montserrat", Arial, sans-serif;
    font-size: 4.6px;
    fill: var(--orange);
    text-anchor: middle;
  }
  .directions-text {
    font-family: "Montserrat", Arial, sans-serif;
    font-size: 8px;
    fill: var(--paper);
  }
  .step-badge { fill: var(--paper); stroke: var(--charcoal); stroke-width: 0.8; }
  .step-art { fill: #e9e9e9; }
  .step-number {
    font-family: "Montserrat", Arial, sans-serif;
    font-size: 9px;
    fill: var(--charcoal);
  }
  .brand-mark { fill: var(--orange); }
</style>
</head>
<body>
<svg class="artboard" viewBox="0 0 1400 981" xmlns="http://www.w3.org/2000/svg">
  <defs>
    <linearGradient id="pvc-window" x1="0" y1="0" x2="1" y2="1">
      <stop offset="0" stop-color="#d9d9d9"/>
      <stop offset="0.45" stop-color="#ffffff"/>
      <stop offset="1" stop-color="#ececec"/>
    </linearGradient>

    <g id="box-dieline">
      <!-- flaps and panels -->
      <rect class="panel" x="232" y="100" width="320" height="107"/>
      <rect class="panel" x="125" y="207" width="534" height="284"/>
      <rect class="panel" x="232" y="491" width="320" height="391"/>

      <!-- front panel: dark spine and orange window frame -->
      <rect class="spine" x="253" y="207" width="112" height="284"/>
      <rect class="band" x="365" y="207" width="187" height="198"/>
      <rect class="window" x="386" y="229" width="146" height="146" fill="url(#pvc-window)"/>

      <text class="tagline">
        <tspan x="309" y="240">The softest,</tspan>
        <tspan x="309" y="253">most absorbent,</tspan>
        <tspan x="309" y="266">lightest, and</tspan>
        <tspan x="309" y="279">safest towel</tspan>
        <tspan x="309" y="292">for your</tspan>
        <tspan x="309" y="305">beautiful hair.</tspan>
      </text>
      <rect class="brand-mark" x="291" y="340" width="36" height="36"/>
      <text class="brand-name" x="238" y="427">THE VOSTRA</text>

      <text class="product-line">
        <tspan x="531" y="388">Microfiber Hair Towel Wrap</tspan>
        <tspan x="531" y="399">Set of 3 Hair Towels</tspan>
      </text>

      <!-- side panel features -->
      <text class="feature-list">
        <tspan x="606" y="289">• Suitable for all hair types</tspan>
        <tspan x="606" y="295">and lengths</tspan>
        <tspan x="606" y="305">• Holds extra-long hair</tspan>
        <tspan x="606" y="317">• Absorbs approximately 70%</tspan>
        <tspan x="606" y="323">of water within 10 minutes</tspan>
        <tspan x="606" y="333">• Reduces risk of split ends,</tspan>
        <tspan x="606" y="339">breakage, and frizz</tspan>
      </text>

      <!-- stripe system across the main row -->
      <rect class="band" x="125" y="430" width="128" height="15"/>
      <rect class="band" x="125" y="455" width="107" height="15"/>
      <rect class="band" x="365" y="430" width="32" height="15"/>
      <rect class="band" x="552" y="430" width="107" height="15"/>
      <rect class="band" x="552" y="455" width="107" height="15"/>
      <rect class="band" x="232" y="445" width="21" height="25"/>
      <rect class="band" x="365" y="455" width="32" height="15"/>
      <rect class="band" x="458" y="420" width="94" height="15"/>
      <rect class="band" x="458" y="420" width="15" height="50"/>
      <rect class="band" x="480" y="448" width="72" height="22"/>
      <rect class="band" x="397" y="420" width="15" height="71"/>
      <rect class="band" x="443" y="445" width="15" height="46"/>

      <!-- bottom panel stripes -->
      <rect class="band" x="397" y="491" width="15" height="109"/>
      <rect class="band" x="443" y="491" width="15" height="109"/>
      <rect class="band" x="365" y="491" width="32" height="30"/>
      <rect class="band" x="412" y="521" width="31" height="30"/>

      <!-- back panel -->
      <rect class="band" x="232" y="600" width="320" height="282"/>
      <rect class="panel" x="412" y="600" width="16" height="282"/>
      <rect class="panel" x="443" y="600" width="15" height="282"/>

      <!-- directions, printed upside down on this panel -->
      <g transform="rotate(180 392 760)">
        <text class="directions-text" x="243" y="652">Towel Measures 26"x10"</text>
        <text class="directions-text" x="243" y="680">Directions:</text>
        <g>
          <circle class="step-badge" cx="419" cy="712" r="23"/>
          <circle class="step-art" cx="413" cy="712" r="15" role="img" aria-label="Step 1: towel draped over the back of the head"/>
          <text class="step-number" x="431" y="716">1</text>
        </g>
        <g>
          <circle class="step-badge" cx="419" cy="770" r="23"/>
          <circle class="step-art" cx="413" cy="770" r="15" role="img" aria-label="Step 2: hair twisted inside the towel"/>
          <text class="step-number" x="431" y="774">2</text>
        </g>
        <g>
          <circle class="step-badge" cx="419" cy="828" r="23"/>
          <circle class="step-art" cx="413" cy="828" r="15" role="img" aria-label="Step 3: towel secured as a wrap"/>
          <text class="step-number" x="431" y="832">3</text>
        </g>
      </g>
    </g>
  </defs>

  <use href="#box-dieline"/>
  <use href="#box-dieline" transform="translate(619.5 0) rotate(180 392 491)"/>
</svg>
</body>
</html>
```